Refresh of The Marston Collective business card

Update business card design using existing primary logo. Names, numbers, etc. are too hard to read on current design.

Target Market(s)

We are a CPA firm.

Industry/Entity Type

Accountant

Contact Information for Business Card

update current card

Colors
0355a3
3176b5
85acd3
0792cd

Requirements
Must have
• Easier to read phone numbers and names
• Use existing logo
Nice to have
• We love our color scheme and current TMC logo. But the names and phone numbers are too small and card just look old and stale.

```html
<!DOCTYPE html>
<html lang="en">
<head>
<meta charset="utf-8">
<title>The Marston Collective – Business Card</title>
<link href="https://fonts.googleapis.com/css2?family=Open+Sans:wght@400;600;700&display=swap" rel="stylesheet">
<style>
  :root {
    --stage: #2b2b2e;
    --navy: #0a2f66;
    --brand-blue: #0355a3;
    --mid-blue: #3176b5;
    --light-blue: #85acd3;
    --sky: #0792cd;
    --paper: #ffffff;
    --rule: #3a3d44;
    --grey-dark: #3e3e40;
  }
  * { box-sizing: border-box; margin: 0; padding: 0; }
  html, body {
    width: 1200px; height: 925px; overflow: hidden;
    background: var(--stage);
    font-family: "Open Sans", Arial, sans-serif;
  }
  .canvas { position: relative; width: 1200px; height: 925px; }

  .card {
    position: absolute; top: 307px;
    width: 540px; height: 310px;
    overflow: hidden;
    box-shadow: 0 10px 30px rgba(0,0,0,.45);
  }

  /* ---------- back of card ---------- */
  .card-back { left: 50px; }
  .card-back .pattern-field {
    position: absolute; inset: 0;
    background: radial-gradient(ellipse at 50% 45%, #b9b9b9 0%, #7d7d7f 35%, var(--grey-dark) 100%);
  }
  .card-back .monogram {
    position: absolute; left: 50%; top: 46%;
    transform: translate(-50%, -50%);
    display: flex; align-items: center; gap: 10px;
  }
  .card-back .monogram-disc {
    width: 58px; height: 58px; border-radius: 50%;
    background: radial-gradient(circle at 40% 35%, var(--mid-blue), var(--navy));
    border: 3px solid #2d2d30;
  }
  .card-back .monogram-name {
    font-weight: 700; font-size: 26px; color: var(--paper); letter-spacing: 2px;
  }
  .card-back .website {
    position: absolute; right: 26px; bottom: 22px;
    font-size: 17px; color: var(--paper); letter-spacing: .5px;
  }

  /* ---------- front of card ---------- */
  .card-front { left: 610px; background: var(--paper); }
  .card-front .shape { position: absolute; inset: 0; }
  .card-front .holder-name {
    position: absolute; left: 26px; top: 26px;
    font-weight: 700; font-size: 22px; color: var(--paper);
  }
  .card-front .contact {
    position: absolute; right: 24px; top: 76px;
    text-align: right; color: var(--paper);
    font-size: 12.5px; line-height: 1.45; font-style: normal;
  }
  .card-front .contact .gap { height: 10px; }
  .card-front .phone-line {
    display: flex; justify-content: flex-end; align-items: center; gap: 7px;
  }
  .card-front .phone-line svg { width: 13px; height: 13px; flex: none; }
  .card-front .email { margin-top: 10px; }

  .card-front .lockup {
    position: absolute; left: 26px; bottom: 34px;
    display: flex; align-items: center; gap: 14px;
  }
  .card-front .lockup-disc {
    width: 62px; height: 62px; border-radius: 50%; flex: none;
    background: radial-gradient(circle at 40% 35%, var(--mid-blue), var(--navy));
    border: 3px solid var(--rule);
  }
  .card-front .lockup-text { color: var(--brand-blue); font-weight: 600; }
  .card-front .lockup-name { font-size: 17px; line-height: 1.1; }
  .card-front .lockup-tag {
    font-size: 7px; letter-spacing: 2px; margin-top: 5px;
    border-top: 1px solid var(--brand-blue); padding-top: 4px;
  }
</style>
</head>
<body>
<main class="canvas">

  <section class="card card-back" aria-label="Back of business card">
    <div class="pattern-field" role="img" aria-label="Faint repeating monogram pattern over a soft grey radial glow"></div>
    <div class="monogram">
      <span class="monogram-disc"></span>
      <span class="monogram-name">TMC</span>
    </div>
    <p class="website">www.marstoncollective.com</p>
  </section>

  <section class="card card-front" aria-label="Front of business card">
    <svg class="shape" viewBox="0 0 540 310" preserveAspectRatio="none" aria-hidden="true">
      <defs>
        <radialGradient id="blueField" cx="0.6" cy="0.35" r="0.8">
          <stop offset="0" stop-color="#1f5fae"/>
          <stop offset="0.6" stop-color="#0a3a7c"/>
          <stop offset="1" stop-color="#082a5a"/>
        </radialGradient>
      </defs>
      <polygon points="0,0 540,0 540,310 360,310 300,190 0,190" fill="url(#blueField)"/>
      <polyline points="0,190 300,190 360,310" fill="none" stroke="#3a3d44" stroke-width="4"/>
    </svg>

    <h1 class="holder-name">Daniel J. Marston, CPA</h1>

    <address class="contact">
      <div>The Marston Collective</div>
      <div>1180 Harbor Pine Rd. Suite 310</div>
      <div>Winter Park, Florida 32789</div>
      <div class="gap"></div>
      <div class="phone-line">321.555.0142
        <svg viewBox="0 0 13 13"><rect width="13" height="13" rx="2" fill="#0792cd"/><path d="M4 3.2l1.3 1.8-.8.9c.5 1.1 1.4 2 2.5 2.5l.9-.8 1.8 1.3-.7 1.2C6.3 9.9 3.3 6.9 3 4z" fill="#fff"/></svg>
      </div>
      <div class="phone-line">321.555.0187
        <svg viewBox="0 0 13 13"><rect width="13" height="13" rx="2" fill="#0792cd"/><rect x="3" y="5" width="7" height="5" fill="#fff"/><rect x="4.5" y="2.5" width="4" height="2.5" fill="#fff"/></svg>
      </div>
      <div class="phone-line">321.555.0163
        <svg viewBox="0 0 13 13"><rect width="13" height="13" rx="2" fill="#0792cd"/><rect x="4.5" y="2.5" width="4" height="8" rx="1" fill="#fff"/></svg>
      </div>
      <div class="phone-line email">dan@marstoncollective.com
        <svg viewBox="0 0 13 13"><rect width="13" height="13" rx="2" fill="#0792cd"/><rect x="2.5" y="4" width="8" height="5.5" fill="#fff"/><path d="M2.5 4l4 3 4-3" fill="none" stroke="#0792cd" stroke-width="1"/></svg>
      </div>
    </address>

    <div class="lockup">
      <span class="lockup-disc"></span>
      <div class="lockup-text">
        <div class="lockup-name">The Marston Collective</div>
        <div class="lockup-tag">CERTIFIED PUBLIC ACCOUNTANTS</div>
      </div>
    </div>
  </section>

</main>
</body>
</html>
```